Stationary Design (using existing logo)

Stationary (print and electronic version for Word/email), envelope, and fax cover. All companies are part of same family or course so designs can be the same, or essentially the same. Use the logos attached, same font and colors.

Target Market(s)

Real estate professionals. Investors and other property owners. Financial professionals.

Industry/Entity Type

Real Estate

Font styles to use
Serif

Requirements
Must have
• Should be a serious, sophisticated design in colors that match the business cards we uploaded. Design needs to match the color and fonts in the attached business cards. Can use the same design for each company, just change logo and color.
Should not have
• Nothing quirky or cute.

```html
<!DOCTYPE html>
<html lang="en">
<head>
<meta charset="utf-8">
<title>Halvern Realty Group – Stationery Set</title>
<link rel="stylesheet" href="https://fonts.googleapis.com/css2?family=Cinzel:wght@500&family=Libre+Caslon+Text&family=Arimo:wght@400;700&display=swap">
<style>
  :root {
    --navy: #1f2f7a;
    --grey-ink: #5f6064;
    --rule: #8a8a8a;
    --backdrop: #c4c4c4;
    --paper: #ffffff;
    --shadow: rgba(0,0,0,0.28);
  }
  * { margin: 0; padding: 0; box-sizing: border-box; }
  html, body { width: 1200px; height: 1200px; overflow: hidden; }
  body { background: var(--backdrop); position: relative; font-family: "Libre Caslon Text", Georgia, serif; }

  .sheet {
    position: absolute; background: var(--paper);
    box-shadow: 6px 8px 10px var(--shadow);
  }
  .letterhead { left: 89px; top: 98px; width: 499px; height: 649px; }
  .fax-cover { left: 619px; top: 101px; width: 499px; height: 646px; }
  .envelope-front { left: 123px; top: 818px; width: 459px; height: 228px; }
  .envelope-back { left: 620px; top: 817px; width: 457px; height: 228px; }

  .wordmark { position: absolute; font-family: "Cinzel", "Times New Roman", serif; font-weight: 500; color: var(--navy); text-align: center; line-height: 1; }
  .wordmark .name { display: block; font-size: 21px; letter-spacing: 1px; }
  .wordmark .sub { display: block; font-size: 8px; letter-spacing: 1.5px; margin-top: 3px; }
  .sheet .wordmark { left: 47px; top: 42px; width: 144px; }

  .header-rule { position: absolute; left: 47px; width: 408px; top: 89px; height: 1px; background: var(--navy); }

  .contact { position: absolute; left: 367px; top: 26px; font-size: 6.4px; color: var(--grey-ink); line-height: 9px; }
  .contact .row { display: flex; align-items: center; gap: 3px; }
  .contact svg { width: 6px; height: 6px; fill: var(--navy); }
  .contact .gap { height: 4px; }
  .contact .address { color: var(--navy); padding-left: 2px; line-height: 7.6px; }

  .fax-table { position: absolute; left: 40px; top: 123px; width: 418px; border-collapse: collapse; font-family: "Arimo", Arial, sans-serif; font-size: 6.8px; font-weight: 700; color: #222; }
  .fax-table td { border: 1px solid #9a9a9a; height: 14.5px; padding: 0 5px; }
  .fax-table .label { width: 47px; }
  .fax-table .field { width: 174px; }

  .routing { position: absolute; left: 40px; top: 210px; width: 418px; height: 364px; border: 1px solid #9a9a9a; }
  .routing-bar { display: flex; height: 15px; background: var(--navy); font-family: "Arimo", Arial, sans-serif; font-weight: 700; font-size: 6.8px; color: #fff; }
  .routing-bar span { display: flex; align-items: center; justify-content: center; gap: 3px; border-right: 1px solid #fff; }
  .routing-bar span:last-child { border-right: none; }
  .routing-bar i { width: 5px; height: 5px; border: 0.8px solid #fff; display: inline-block; }
  .comments-label { text-align: center; font-family: "Arimo", Arial, sans-serif; font-size: 7px; color: #222; margin-top: 12px; }

  .envelope-front .wordmark { left: 41px; top: 25px; width: 90px; }
  .envelope-front .wordmark .name { font-size: 13px; letter-spacing: 0.5px; }
  .envelope-front .wordmark .sub { font-size: 5px; letter-spacing: 1px; margin-top: 2px; }
  .return-address { position: absolute; left: 17px; top: 55px; font-size: 7px; line-height: 9.5px; color: var(--navy); }

  .flap { position: absolute; left: 0; top: 0; width: 457px; height: 64px; }
  .envelope-back .wordmark { left: 178px; top: 31px; width: 100px; }
  .envelope-back .wordmark .name { font-size: 11px; letter-spacing: 1px; }
</style>
</head>
<body>

<section class="sheet letterhead" aria-label="Letterhead">
  <div class="wordmark"><span class="name">HALVERN</span><span class="sub">REALTY GROUP LLC</span></div>
  <div class="contact">
    <div class="row"><svg viewBox="0 0 10 10"><path d="M1 3 Q5 0 9 3 L8 5 L6 4 L6 3 L4 3 L4 4 L2 5 Z M3 5 H7 V9 H3 Z"/></svg>555.201.4410</div>
    <div class="row"><svg viewBox="0 0 10 10"><rect x="2" y="1" width="6" height="4"/><rect x="1" y="5" width="8" height="4"/></svg>555.201.4411</div>
    <div class="gap"></div>
    <div class="row"><svg viewBox="0 0 10 10"><circle cx="5" cy="5" r="4" fill="none" stroke="#1f2f7a" stroke-width="1.4"/></svg>www.halvernrealty.com</div>
    <div class="gap"></div>
    <div class="address">1480 W Alder Ave.<br>Springfield, IL 62704</div>
  </div>
  <div class="header-rule"></div>
</section>

<section class="sheet fax-cover" aria-label="Fax cover sheet">
  <div class="wordmark"><span class="name">HALVERN</span><span class="sub">REALTY GROUP LLC</span></div>
  <div class="contact">
    <div class="row"><svg viewBox="0 0 10 10"><path d="M1 3 Q5 0 9 3 L8 5 L6 4 L6 3 L4 3 L4 4 L2 5 Z M3 5 H7 V9 H3 Z"/></svg>555.201.4410</div>
    <div class="row"><svg viewBox="0 0 10 10"><rect x="2" y="1" width="6" height="4"/><rect x="1" y="5" width="8" height="4"/></svg>555.201.4411</div>
    <div class="gap"></div>
    <div class="row"><svg viewBox="0 0 10 10"><circle cx="5" cy="5" r="4" fill="none" stroke="#1f2f7a" stroke-width="1.4"/></svg>www.halvernrealty.com</div>
    <div class="gap"></div>
    <div class="address">1480 W Alder Ave.<br>Springfield, IL 62704</div>
  </div>
  <div class="header-rule"></div>

  <table class="fax-table">
    <tr><td class="label">To:</td><td class="field"></td><td class="label">From:</td><td></td></tr>
    <tr><td class="label">Fax:</td><td class="field"></td><td class="label">Pages:</td><td></td></tr>
    <tr><td class="label">Phone:</td><td class="field"></td><td class="label">Date:</td><td></td></tr>
    <tr><td class="label">Re:</td><td class="field"></td><td class="label">CC:</td><td></td></tr>
  </table>

  <div class="routing">
    <div class="routing-bar">
      <span style="width:77px"><i></i>Urgent</span>
      <span style="width:84px"><i></i>For Review</span>
      <span style="width:98px"><i></i>Please Comment</span>
      <span style="width:82px"><i></i>Please Reply</span>
      <span style="width:77px"><i></i>Confidential</span>
    </div>
    <div class="comments-label">COMMENTS:</div>
  </div>
</section>

<section class="sheet envelope-front" aria-label="Envelope front">
  <div class="wordmark"><span class="name">HALVERN</span><span class="sub">REALTY GROUP LLC</span></div>
  <div class="return-address">1480 W Alder Ave.<br>Springfield, IL 62704</div>
</section>

<section class="sheet envelope-back" aria-label="Envelope back">
  <svg class="flap" viewBox="0 0 457 64">
    <path d="M2 0 Q14 50 40 61 L420 60 Q442 52 455 0" fill="none" stroke="#8a8a8a" stroke-width="0.9"/>
  </svg>
  <div class="wordmark"><span class="name">HALVERN</span></div>
</section>

</body>
</html>
```